Australian residential property business needs a business card design

I need a business card design for my new business 'Harbour Estate Ventures'. The business will involve house purchases, land development sites, renovation projects, sub-divisions etc. I will be buying property from motivated vendors and working with property investors. I will deal with a wide range of people working in the residential property market including real estate agents, councils, tradespeople, banks, home owners, etc.

I would like something simple, not flashy, but a little bit unique. The colours should be in line with my logo. The business card needs to be professional. I would like something memorable, but not 'busy' or too bright. Not boring. Modern ok.

Target Market(s)

Home owners looking to sell their property, real estate agents, tradespeople (e.g. plumbers, builders, electricians etc), property investors, local councils, and anyone else involved in the residential property industry

Industry/Entity Type

Business

Contact Information for Business Card

I need to include my business name/logo, my name, my title, a PO Box number/address, a mobile number, and an email address.

Font styles to use
Serif

Requirements
Must have
• My business card details listed above.

```html
<!DOCTYPE html>
<html lang="en">
<head>
<meta charset="utf-8">
<title>Harbour Estate Ventures – Business Card</title>
<link rel="stylesheet" href="https://fonts.googleapis.com/css2?family=Arimo:wght@400;700&display=swap">
<style>
  :root {
    --mustard: #ecbf3b;
    --leaf: #56b847;
    --ink-green: #2e9a48;
    --paper: #ffffff;
    --accent-orange: #f2a52a;
  }
  * { margin: 0; padding: 0; box-sizing: border-box; }
  html, body {
    width: 1200px;
    height: 740px;
    overflow: hidden;
    background: var(--paper);
  }
  .card {
    position: relative;
    width: 1200px;
    height: 740px;
    font-family: "Arimo", Arial, sans-serif;
    color: var(--ink-green);
    overflow: hidden;
  }
  .card__contact-side {
    position: absolute;
    left: 0; top: 0;
    width: 660px; height: 740px;
    background: linear-gradient(to bottom,
      var(--mustard) 0, var(--mustard) 520px,
      var(--leaf) 665px, var(--leaf) 740px);
  }
  .card__brand-side {
    position: absolute;
    left: 660px; top: 0;
    width: 540px; height: 740px;
    background: linear-gradient(to bottom,
      var(--paper) 0, var(--paper) 525px,
      var(--leaf) 665px, var(--leaf) 740px);
  }
  .holder-name {
    position: absolute;
    left: 0; width: 705px;
    top: 160px;
    text-align: center;
    font-size: 56px;
    line-height: 1;
  }
  .holder-title {
    position: absolute;
    left: 0; width: 714px;
    top: 230px;
    text-align: center;
    font-size: 37px;
    line-height: 1;
  }
  .contact-line {
    position: absolute;
    display: flex;
    align-items: center;
    font-size: 42px;
    line-height: 1;
    white-space: nowrap;
  }
  .contact-line--address { left: 195px; top: 388px; }
  .contact-line--phone { left: 168px; top: 448px; }
  .contact-line--email { left: 258px; top: 510px; }
  .contact-icon { fill: var(--ink-green); margin-right: 10px; }
  .brand {
    position: absolute;
    left: 660px; width: 540px;
    top: 262px;
    display: flex;
    flex-direction: column;
    align-items: center;
  }
  .brand__mark {
    width: 64px; height: 64px;
    background: var(--accent-orange);
    margin-bottom: 46px;
  }
  .brand__name {
    font-size: 34px;
    font-weight: 700;
    color: var(--ink-green);
    letter-spacing: 0.5px;
  }
</style>
</head>
<body>
  <main class="card">
    <section class="card__contact-side">
      <h1 class="holder-name">my name</h1>
      <p class="holder-title">director</p>

      <p class="contact-line contact-line--address">PO box/address</p>

      <p class="contact-line contact-line--phone">
        <svg class="contact-icon" width="40" height="52" viewBox="0 0 40 52" aria-hidden="true">
          <path d="M9 2 L16 2 L18 14 L13 17 C13 26 17 33 23 38 L28 34 L37 41 L34 50 C20 50 4 34 4 14 C4 8 6 4 9 2 Z"/>
        </svg>
        phone number
      </p>

      <p class="contact-line contact-line--email">
        <svg class="contact-icon" width="52" height="34" viewBox="0 0 52 34" aria-hidden="true">
          <path d="M0 0 H52 V34 H0 Z M3 3 L26 20 L49 3 Z M0 32 L19 16 L3 4 Z M52 32 L33 16 L49 4 Z" fill-rule="evenodd"/>
        </svg>
        email
      </p>
    </section>

    <section class="card__brand-side"></section>

    <div class="brand">
      <span class="brand__mark" aria-hidden="true"></span>
      <span class="brand__name">Harbour Estate Ventures</span>
    </div>
  </main>
</body>
</html>
```